Book cover for a book on tactics, habits and directives learned from world class performers

The Quiet Ledger book is the first in a series of four books filled with proven tactics, habits and directives (i.e., what to do) that young, ambitious working professionals should be doing to make their life better. The first book is on foundational or keystone habits - that is, the habits that will help everyone upgrade their life and enable other great habits in their life (things such as waking up early in the morning or exercising)

The goal of the book is to stand out on the Brimvale platform as a small thumbnail, as well as a 5 x 8 book.

The imagery should make the viewer feel that the book (and the author) are the authority in habits and developing habits.

The reader should feel that they must have this book if they know they should be developing successful habits but do not want to comb through hundreds of books just to find the one tactic or habit that they should be doing. It's important that the book "pops off the shelf" and catches the eye quickly.

The most important part of the design is that it sells, not that it looks well-designed. I am open to any image or illustration you choose though please consider the nice have I have listed below. Here are a few words that come to mind when thinking of my book: growth, self development, leadership, success, freedom, passion, motivation, young professional, accomplished, experience.

I like a bold color palette. I like bold titles that you know right away what the title is and what it is about, not too busy and with simple color schemes. 2 - 3 colors.

Books with covers I like:
- Lamp Orchard by Norris Pellaquin
- Under The Copper Tide by Gordon Pruitt
- The Velvet Compass by Edgar Fulbright

Target Market(s)

- Young 20 - 40 year old ambitious working professionals interested in self development and listen to podcasts of Ned Caplow, Rufus Denholme
- Just starting out management consultants

Colors

Designer to choose colors to be used in the design.

Requirements
Must have
• 'Quiet Ledger' title - first and foremost
• Author name - Lu Qiao - probably on the bottom or somewhere
• Bold colour / colours or a graphic that is eye catching (and makes it different from other habits books on Brimvale)
Nice to have
• Would like to have some sort of visual, colour or theme that can run through the four books - would be great to have a cover design that can be simply changed to depict the second, third or fourth book in the series - maybe the graphic or visual can be changed with some colours, etc. but with the overall feel looking similar so that people can see that it's part of the same book series

```html
<!DOCTYPE html>
<html lang="en">
<head>
<meta charset="utf-8">
<title>Quiet Ledger — Lu Qiao</title>
<link rel="stylesheet" href="https://fonts.googleapis.com/css2?family=Roboto+Condensed:wght@700&family=Roboto:wght@400&display=swap">
<style>
  :root {
    --cover-grey: #d0d0d0;
    --ink: #000000;
  }
  * { margin: 0; padding: 0; box-sizing: border-box; }
  html, body {
    width: 777px;
    height: 1200px;
    overflow: hidden;
    background: var(--cover-grey);
  }
  .cover {
    position: relative;
    width: 777px;
    height: 1200px;
    background: var(--cover-grey);
    color: var(--ink);
  }
  .cover__mark {
    position: absolute;
    left: 0;
    top: 0;
    width: 777px;
    height: 1200px;
  }
  .cover__mark path,
  .cover__mark ellipse { fill: var(--ink); }
  .cover__title {
    position: absolute;
    left: 0;
    right: 0;
    top: 820px;
    text-align: center;
    font-family: "Roboto Condensed", "Arial Narrow", sans-serif;
    font-weight: 700;
    font-size: 72px;
    line-height: 1;
    letter-spacing: 1.5px;
  }
  .cover__author {
    position: absolute;
    left: 0;
    right: 0;
    top: 970px;
    text-align: center;
    font-family: "Roboto", Arial, sans-serif;
    font-weight: 400;
    font-size: 41px;
    line-height: 1;
  }
</style>
</head>
<body>
  <main class="cover">
    <svg class="cover__mark" viewBox="0 0 849 1312" aria-hidden="true">
      <path d="M300,300 C285,300 278,288 280,270 C285,240 330,175 432,175 C530,175 590,235 590,310 C590,370 565,405 525,437 C490,465 475,478 460,497 C440,520 430,555 430,627 L405,627 C405,540 420,505 450,470 C470,448 490,430 505,410 C530,385 542,352 542,310 C542,245 510,200 432,200 C370,200 345,240 320,285 C314,295 308,300 300,300 Z"/>
      <ellipse cx="418" cy="717" rx="34" ry="37"/>
    </svg>
    <h1 class="cover__title">Quiet Ledger</h1>
    <p class="cover__author">Lu Qiao</p>
  </main>
</body>
</html>
```